Local Storage Space Company needs a one page, 2 sided flyer design

We need to have a one page, double sided flyer design.

Have attached our company profile for your viewing.

Industry/Entity Type

It Company

Requirements
Must have
• must draw the information from the attached file or website: www.keepvaultbox.example

```html
<!DOCTYPE html>
<html lang="en">
<head>
<meta charset="utf-8">
<title>Keepvaultbox – Storage Flyer</title>
<link href="https://fonts.googleapis.com/css2?family=Lato:ital,wght@0,400;0,700;0,900;1,400;1,700&display=swap" rel="stylesheet">
<style>
:root{
  --green:#6cb52d;
  --green-light:#9fd44a;
  --blue:#0a6fd1;
  --blue-dark:#0a3f9c;
  --ink:#222;
  --grey-text:#5a5a5a;
  --paper:#ffffff;
  --paper-shade:#d9d9d9;
  --stage:#e9e9e9;
}
*{box-sizing:border-box;margin:0;padding:0}
html,body{width:1200px;height:900px;overflow:hidden}
body{background:var(--stage);font-family:'Lato',sans-serif;color:var(--ink);position:relative}
.page{position:absolute;width:500px;height:640px;background:linear-gradient(160deg,var(--paper) 30%,var(--paper-shade));overflow:hidden;box-shadow:0 2px 8px rgba(0,0,0,.15)}
.page--front{left:55px;top:80px}
.page--back{left:640px;top:85px}
.page svg.art{position:absolute;left:0;top:0}
.side-label{position:absolute;top:785px;font-weight:700;font-size:28px;color:#444;letter-spacing:.5px}
.side-label--front{left:230px}
.side-label--back{left:842px}

/* front */
.headline{position:absolute;right:40px;top:448px;text-align:right;line-height:1}
.headline__lead{font-size:40px;color:var(--grey-text);font-weight:400}
.headline__main{font-size:54px;color:var(--green);font-weight:700;margin-top:8px}
.headline__sub{font-size:44px;color:var(--blue);font-weight:900;margin-top:6px}
.brand{position:absolute;left:28px;top:555px;display:flex;align-items:center;gap:8px}
.brand__dot{width:40px;height:40px;border-radius:50%;background:var(--blue)}
.brand__name{font-size:16px;font-weight:700;color:var(--green);letter-spacing:.3px}
.brand__tag{font-size:6px;color:var(--green);letter-spacing:1.5px;margin-top:2px}

/* back */
.about{position:absolute;right:16px;top:40px;width:400px;text-align:right}
.about__title{font-size:18px;font-weight:900;color:var(--green);margin-bottom:6px}
.about p{font-size:8.4px;line-height:1.25;margin-bottom:6px}
.estimator{position:absolute;left:20px;top:190px;font-size:16px;font-weight:900;color:var(--green)}
.unit{position:absolute;width:140px;font-size:10px;line-height:1.2}
.unit__title{font-size:10px;font-weight:900;color:var(--blue);margin-bottom:2px}
.unit__row{display:flex;align-items:baseline}
.unit__row .fill{flex:1;border-bottom:1px dotted var(--ink);margin:0 1px 2px}
.unit__desc{display:flex;gap:6px;margin-top:10px}
.unit__desc-label{color:var(--green);font-weight:700}
.unit__desc-text{text-align:right;flex:1}
.unit__desc-text em{font-style:italic}
.unit--1{left:22px;top:208px}
.unit--2{left:172px;top:214px}
.unit--3{left:16px;top:340px}
.unit--4{left:168px;top:352px}
.note{position:absolute;left:22px;top:535px;font-size:7px}
.promo{position:absolute;left:40px;top:548px;width:300px;text-align:center;font-size:10.5px;color:var(--blue);line-height:1.3}
.promo strong{font-style:italic;font-weight:900}
.footer{position:absolute;left:0;bottom:0;width:100%;height:62px;background:var(--green);border-top:4px solid var(--blue);padding:6px 14px;color:#fff;font-size:7px;line-height:1.55}
.footer__row{display:flex;align-items:center;gap:6px}
.footer__icon{width:7px;height:7px}
</style>
</head>
<body>

<section class="page page--front">
  <svg class="art" width="500" height="640" viewBox="0 0 500 640">
    <defs>
      <linearGradient id="warehouseTone" x1="0" y1="0" x2="1" y2="1">
        <stop offset="0" stop-color="#c9b8a0"/>
        <stop offset=".5" stop-color="#7d8fa8"/>
        <stop offset="1" stop-color="#b57b4a"/>
      </linearGradient>
      <linearGradient id="greenSweep" x1="0" y1="0" x2="1" y2="1">
        <stop offset="0" stop-color="var(--green-light)"/>
        <stop offset="1" stop-color="var(--green)"/>
      </linearGradient>
    </defs>
    <path d="M0 0 H440 C470 120 430 230 360 290 C320 325 300 300 270 320 C230 350 160 370 110 360 C60 350 20 340 0 330 Z" fill="#1e4fb0"/>
    <path d="M0 0 H400 C430 80 410 180 340 250 C300 290 270 270 240 300 C200 335 120 340 20 320 L0 315 Z" fill="url(#warehouseTone)" role="img" aria-label="Photo of tall warehouse racking stacked with boxes"/>
    <path d="M405 0 H470 C500 110 470 230 400 300 C360 345 300 350 250 370 C210 390 170 390 150 380 C200 370 240 340 280 300 C300 280 330 260 360 220 C420 150 430 70 405 0 Z" fill="url(#greenSweep)"/>
    <path d="M10 325 C60 350 110 360 160 355 C200 350 230 330 250 315 C240 345 200 380 140 385 C80 390 30 360 10 325 Z" fill="var(--green)"/>
    <path d="M435 0 H500 V40 C480 20 455 8 435 0 Z" fill="var(--blue)"/>
  </svg>
  <div class="headline">
    <div class="headline__lead">We are your</div>
    <div class="headline__main">Storage</div>
    <div class="headline__sub">SOLUTION</div>
  </div>
  <div class="brand">
    <span class="brand__dot"></span>
    <div>
      <div class="brand__name">KEEPVAULTBOX</div>
      <div class="brand__tag">YOUR STORAGE SOLUTION</div>
    </div>
  </div>
</section>

<section class="page page--back">
  <svg class="art" width="500" height="640" viewBox="0 0 500 640">
    <defs>
      <linearGradient id="aisleTone" x1="0" y1="0" x2="1" y2="1">
        <stop offset="0" stop-color="#e2e0d2"/>
        <stop offset=".5" stop-color="#8f9a8a"/>
        <stop offset="1" stop-color="#c9c6b8"/>
      </linearGradient>
    </defs>
    <path d="M0 0 H120 C80 30 60 80 40 120 C25 150 10 150 0 150 Z" fill="var(--green)"/>
    <path d="M0 0 H70 C40 30 25 70 15 100 C10 115 5 120 0 120 Z" fill="var(--blue)"/>
    <path d="M100 0 H170 C130 20 110 50 95 80 C90 50 92 20 100 0 Z" fill="var(--green-light)"/>
    <path d="M500 255 C430 260 360 300 340 360 C320 420 320 520 330 590 H500 Z" fill="var(--green)"/>
    <path d="M500 290 C440 300 390 340 375 390 L365 590 H500 Z" fill="var(--blue)"/>
    <path d="M500 320 C455 330 410 360 395 410 C385 450 388 540 395 590 H500 Z" fill="url(#aisleTone)" role="img" aria-label="Photo of a long warehouse aisle lined with storage racks"/>
  </svg>

  <div class="about">
    <h2 class="about__title">ABOUT US</h2>
    <p>Keepvaultbox is a storage operator in Singapore.</p>
    <p>At Keepvaultbox, we aim to help you organise your work or living spaces, to restore for you a peace of mind when you require additional space.</p>
    <p>Instead of squeezing your items with you, store them with us in our warehouse that can be easily accessed 24-hours a day and also fitted with 24-hours security. Our self-storage facility is conveniently located off city-center near expressways and accessible via public transportation.</p>
    <p>Our warehouse has individual storage units at various sizes, and you can opt for air-conditioned or non-air conditioned units. Rates are affordable and you can choose from flexible time periods (ranging from a few weeks to months and years) to best suit your needs.</p>
  </div>

  <h2 class="estimator">UNIT SIZE ESTIMATOR</h2>

  <div class="unit unit--1">
    <div class="unit__title">SIZE 1</div>
    <div class="unit__row">Length<span class="fill"></span>7.25 ft</div>
    <div class="unit__row">Width<span class="fill"></span>2.92 ft</div>
    <div class="unit__row">Height<span class="fill"></span>8.4 ft</div>
    <div class="unit__row">Total Floor Area<span class="fill"></span>21.27 sqft</div>
    <div class="unit__row">Total Volume<span class="fill"></span>177.83 X³</div>
    <div class="unit__desc"><span class="unit__desc-label">Description:</span><span class="unit__desc-text">Approximately the size of a phonebooth</span></div>
  </div>

  <div class="unit unit--2">
    <div class="unit__title">SIZE 2</div>
    <div class="unit__row">Length<span class="fill"></span>9.83 ft</div>
    <div class="unit__row">Width<span class="fill"></span>4.83 ft</div>
    <div class="unit__row">Height<span class="fill"></span>8.4 ft</div>
    <div class="unit__row">Total Floor Area<span class="fill"></span>47.48 sqft</div>
    <div class="unit__row">Total Volume<span class="fill"></span>398.83 X³</div>
    <div class="unit__desc"><span class="unit__desc-label">Description:</span><span class="unit__desc-text">Approximately the size of a 1 bedroom</span></div>
  </div>

  <div class="unit unit--3">
    <div class="unit__title">SIZE 3</div>
    <div class="unit__row">Length<span class="fill"></span>9.75 ft</div>
    <div class="unit__row">Width<span class="fill"></span>9.75 ft</div>
    <div class="unit__row">Height<span class="fill"></span>8.4 ft</div>
    <div class="unit__row">Total Floor Area<span class="fill"></span>95.06 sqft</div>
    <div class="unit__row">Total Volume<span class="fill"></span>798.50 X³</div>
    <div class="unit__desc"><span class="unit__desc-label">Description:</span><span class="unit__desc-text">Approximately 300 to 400 document boxes <em>(Dimensions of document box: 42 x 34 x 26cm)</em> or Five pallets of stock stacked on the floor</span></div>
  </div>

  <div class="unit unit--4">
    <div class="unit__title">SIZE 4</div>
    <div class="unit__row">Length<span class="fill"></span>21.25 ft</div>
    <div class="unit__row">Width<span class="fill"></span>9.75 ft</div>
    <div class="unit__row">Height<span class="fill"></span>8.4 ft</div>
    <div class="unit__row">Total Floor Area<span class="fill"></span>207.19 sqft</div>
    <div class="unit__row">Total Volume<span class="fill"></span>1740.38 X³</div>
    <div class="unit__desc"><span class="unit__desc-label">Description:</span><span class="unit__desc-text">Approximately the contents of a 3 bedroom house Or Approximately 900-1000 document boxes</span></div>
  </div>

  <p class="note">* Sizes may vary for actual space available</p>
  <p class="promo">From time to time, <strong>WE PROVIDE ATTRACTIVE PROMOTION</strong><br>Please Call Or Email In For Updates!</p>

  <footer class="footer">
    <div class="footer__row">
      <svg class="footer__icon" viewBox="0 0 10 10"><path d="M5 0 L10 5 H8.5 V10 H1.5 V5 H0 Z" fill="#fff"/></svg>
      Alder Industrial Building, #04-12, 18 Kestrel Lane, Singapore 349120
    </div>
    <div class="footer__row">
      <svg class="footer__icon" viewBox="0 0 10 10"><rect x="0" y="2" width="10" height="7" fill="#fff"/><path d="M0 2 L5 6 L10 2" stroke="var(--green)" fill="none"/></svg>
      enquires@keepvaultbox.example
    </div>
    <div class="footer__row">
      <svg class="footer__icon" viewBox="0 0 10 10"><circle cx="5" cy="5" r="4.3" stroke="#fff" fill="none"/><path d="M1 5 H9 M5 1 V9" stroke="#fff"/></svg>
      www.keepvaultbox.example
    </div>
  </footer>
</section>

<div class="side-label side-label--front">Front</div>
<div class="side-label side-label--back">Back</div>

</body>
</html>
```